Bitcoin Wallet & KORVA Landing Page

We need a landing page (one-pager) for our bitcoin wallet. we offer an online bitcoin wallet and an KORVA prepaid card with which you can spend your bitcoins. Have similar offers: zelomint, dravu, lunekora, pemtor Name will be: Quarlen

Industry/Entity Type

Online

Logo Text

Quarlen

Coding

Coded - Design and coding required

Number of Pages Required

1 page

Font styles to use
Sans Serif

Colors
3176b5
33a6d7

```html
<!DOCTYPE html>
<html lang="en">
<head>
<meta charset="utf-8">
<title>Quarlen — Bitcoin Wallet &amp; KORVA Card</title>
<link rel="stylesheet" href="https://fonts.googleapis.com/css2?family=Source+Sans+3:wght@400;600;700&display=swap">
<style>
:root{
  --blue:#3176b5;
  --sky:#33a6d7;
  --ink:#1a1a1a;
  --dark:#1c1c1e;
  --darker:#141416;
  --text:#555b61;
  --muted:#9aa0a6;
  --light:#f0f1f3;
  --white:#ffffff;
  --faq:#254a66;
}
*{box-sizing:border-box;margin:0;padding:0}
html,body{width:1200px;height:3200px;overflow:hidden}
body{font-family:"Source Sans 3",Arial,sans-serif;color:var(--text);background:var(--white)}
.page{position:relative;width:1200px;height:3200px;overflow:hidden}

/* Hero */
.hero{position:relative;height:600px;background:linear-gradient(180deg,#232325 0%,#19191b 100%);color:var(--white)}
.nav{position:absolute;top:0;left:0;right:0;height:72px;display:flex;align-items:center;padding:0 80px;border-bottom:1px solid rgba(255,255,255,.08)}
.brand{display:flex;align-items:center;gap:12px;font-weight:700;font-size:30px;color:var(--white)}
.brand-mark{width:28px;height:28px;background:var(--sky);border-radius:4px}
.nav-links{margin-left:auto;display:flex;gap:26px;list-style:none;font-size:14px;font-weight:600;letter-spacing:.5px}
.hero-copy{position:absolute;left:100px;top:150px;width:440px}
.hero-title{font-size:64px;font-weight:600;line-height:1}
.hero-text{margin-top:34px;font-size:18px;line-height:1.5;font-weight:600}
.btn{display:inline-block;background:var(--blue);color:var(--white);border-radius:24px;font-weight:600;font-size:16px;padding:13px 34px}
.hero .btn{margin-top:34px}
.dots{position:absolute;left:100px;top:555px;display:flex;gap:6px}
.dots span{width:12px;height:12px;border:2px solid var(--white);border-radius:50%}
.dots span:first-child{background:var(--white)}
.hero-art{position:absolute;left:620px;top:72px;width:500px;height:480px;background:radial-gradient(circle at 60% 55%,#5a4a2a 0%,#2b2a29 45%,#1c1c1e 75%);border-radius:4px}

/* Features */
.features{height:600px;padding-top:70px;text-align:center}
.section-title{font-size:30px;font-weight:700;color:var(--sky);letter-spacing:.5px}
.rule{width:60px;height:2px;background:var(--sky);margin:18px auto 0}
.feature-row{display:flex;justify-content:center;gap:80px;margin-top:50px}
.feature{width:240px}
.feature-icon{width:170px;height:170px;margin:0 auto;border-radius:50%;border:3px solid var(--sky);display:flex;align-items:center;justify-content:center}
.feature-icon.filled{background:var(--sky)}
.feature-icon i{display:block;width:100px;height:80px;border-radius:8px;background:linear-gradient(135deg,#e9b94a,#d9534f)}
.feature-icon.filled i{background:linear-gradient(135deg,#f5f5f5,#f0a04b)}
.feature h3{margin-top:30px;font-size:21px;line-height:1.25;color:var(--sky);font-weight:600}
.feature p{margin-top:28px;font-size:13px;line-height:1.5;color:var(--muted)}

/* Testimonials & FAQ */
.split{height:600px;background:var(--dark);color:var(--white);display:flex;padding:70px 100px 0;gap:80px}
.split h2{font-size:26px;font-weight:700;letter-spacing:.5px}
.split .rule{margin:16px 0 0}
.testimonials{width:440px}
.quote{margin-top:36px;font-size:60px;line-height:.6;font-weight:700}
.testimonials p{margin-top:16px;font-size:15px;line-height:1.6;color:#d5d7da}
.person{display:flex;align-items:center;gap:24px;margin-top:34px}
.avatar{width:130px;height:130px;border-radius:50%;border:4px solid var(--white);background:linear-gradient(160deg,#b98a6a,#4a3a32)}
.person strong{display:block;font-size:26px}
.person span{font-size:15px;color:#c9cbce}
.split .dots{position:static;margin-top:30px}
.faq{flex:1}
.faq-intro{margin-top:34px;font-size:15px;line-height:1.6;color:#d5d7da}
.faq-item{display:flex;align-items:center;gap:22px;margin-top:26px;font-size:14px;line-height:1.5;color:#d5d7da}
.faq-item svg{flex:none}
.faq-item.open{margin-left:-4px;background:var(--faq);padding:16px 20px;border-radius:4px}

/* Wallet */
.wallet{height:400px;display:flex;padding:70px 100px 0;gap:90px}
.wallet-copy{width:500px}
.wallet h2{font-size:36px;color:var(--sky);font-weight:700;line-height:1.2}
.wallet .rule{margin:16px 0 0}
.wallet p{margin-top:26px;font-size:14px;line-height:1.6;color:var(--text)}
.wallet .btn{margin-top:26px;font-size:15px;padding:12px 28px}
.wallet-art{width:400px;height:260px;margin-top:0;background:linear-gradient(180deg,#dfe8ef 0%,#b6c3cc 100%);border-radius:10px}

/* Ratings */
.ratings{height:500px;background:var(--light);padding-top:50px;text-align:center}
.ratings .section-title{font-size:34px}
.cards{display:flex;justify-content:center;gap:30px;margin-top:56px}
.card{width:330px}
.card-box{position:relative;height:170px;border:3px solid var(--sky);background:var(--white);padding:46px 30px 0;font-size:13px;line-height:1.5;color:var(--text)}
.card.featured .card-box{background:var(--blue);border-color:var(--blue);color:var(--white)}
.card-icon{position:absolute;top:-24px;left:50%;margin-left:-24px;width:48px;height:48px;border-radius:50%;background:var(--white);border:3px solid var(--sky);display:flex;align-items:center;justify-content:center}
.card h4{margin-top:20px;font-size:17px;font-weight:600;color:var(--sky)}
.stars{margin-top:6px;color:var(--blue);font-size:18px;letter-spacing:2px}

/* CTA */
.cta{height:90px;background:var(--blue);color:var(--white);display:flex;align-items:center;justify-content:center;gap:70px;font-size:16px;font-weight:600}
.btn-outline{border:2px solid var(--white);border-radius:22px;padding:9px 30px}

/* Footer */
.footer{height:410px;background:var(--darker);color:var(--white);text-align:center;padding-top:50px}
.footer .brand{justify-content:center;font-size:32px}
.social{display:flex;justify-content:center;gap:14px;margin-top:30px}
.social span{width:40px;height:40px;border:2px solid var(--white);border-radius:50%}
.footer-links{display:flex;justify-content:center;gap:30px;list-style:none;margin-top:60px;font-size:14px;font-weight:700;letter-spacing:.5px}
.footer hr{width:1000px;margin:30px auto 0;border:0;border-top:1px solid rgba(255,255,255,.12)}
.copyright{margin-top:26px;font-size:13px;font-weight:600}
</style>
</head>
<body>
<div class="page">

<header class="hero">
  <nav class="nav">
    <div class="brand"><span class="brand-mark"></span>Quarlen</div>
    <ul class="nav-links">
      <li>HOME</li><li>QUARLEN FEATURES</li><li>FAQ</li><li>TESTIMONIALS</li><li>YOUR WALLET</li><li>RATINGS</li><li>CONTACT</li>
    </ul>
  </nav>
  <div class="hero-copy">
    <h1 class="hero-title">Quarlen</h1>
    <p class="hero-text">We offer an online bitcoin wallet and an KORVA prepaid card with which you can spend your bitcoins.</p>
    <span class="btn">Read More</span>
  </div>
  <div class="hero-art" role="img" aria-label="Line illustration of hanging bitcoin coins above a hand holding a glowing gold coin"></div>
  <div class="dots"><span></span><span></span><span></span><span></span><span></span></div>
</header>

<section class="features">
  <h2 class="section-title">QUARLEN FEATURES</h2>
  <div class="rule"></div>
  <div class="feature-row">
    <div class="feature">
      <div class="feature-icon"><i role="img" aria-label="Illustration of a shop with digital coins"></i></div>
      <h3>Use digital currency in the real world</h3>
      <p>Duis aute irure dolor in reprehenderit in volup tate velit esse cillum dolore eu fugiat nulla pariatur.</p>
    </div>
    <div class="feature">
      <div class="feature-icon filled"><i role="img" aria-label="Illustration of a computer screen with payment cards"></i></div>
      <h3>Buy Bitcoins with debit or credit card</h3>
      <p>Duis aute irure dolor in reprehenderit in volup tate velit esse cillum dolore eu fugiat nulla pariatur.</p>
    </div>
    <div class="feature">
      <div class="feature-icon"><i role="img" aria-label="Illustration of a wallet with cards and currency"></i></div>
      <h3>Exchange currencies – save fees</h3>
      <p>Duis aute irure dolor in reprehenderit in volup tate velit esse cillum dolore eu fugiat nulla pariatur.</p>
    </div>
  </div>
</section>

<section class="split">
  <div class="testimonials">
    <h2>TESTIMONIALS</h2>
    <div class="rule"></div>
    <div class="quote">&ldquo;</div>
    <p>Neque porro quisquam est, qui dolorem ipsum quia dolor sit amet, consectetur, adipisci velit, sed quia non numquam eius modi tempora incidunt.</p>
    <div class="person">
      <div class="avatar" role="img" aria-label="Portrait photo of the customer"></div>
      <div><strong>Jenny</strong><span>Manager</span></div>
    </div>
    <div class="dots"><span></span><span></span><span></span><span></span><span></span></div>
  </div>
  <div class="faq">
    <h2>FREQUENTLY ASKED QUESTIONS</h2>
    <div class="rule"></div>
    <p class="faq-intro">Neque porro quisquam est, qui dolorem ipsum quia dolor sit amet, consectetur, adipisci velit.</p>
    <div class="faq-item">
      <svg width="44" height="44" viewBox="0 0 44 44"><circle cx="22" cy="22" r="22" fill="#33a6d7"/><path d="M14 22h16M22 14v16" stroke="#fff" stroke-width="3"/></svg>
      <span>Neque porro quisquam est, qui dolorem ipsum quia dolor sit amet, consectetur.</span>
    </div>
    <div class="faq-item open">
      <span>Neque porro quisquam est, qui dolorem ipsum quia dolor sit amet, consectetur, adipisci velit, sed quia non numquam.</span>
    </div>
    <div class="faq-item">
      <svg width="44" height="44" viewBox="0 0 44 44"><circle cx="22" cy="22" r="22" fill="#33a6d7"/><path d="M14 22h16" stroke="#fff" stroke-width="3"/></svg>
      <span>Neque porro quisquam est, qui dolorem ipsum quia dolor sit amet, consectetur.</span>
    </div>
  </div>
</section>

<section class="wallet">
  <div class="wallet-copy">
    <h2>Your wallet to pay bills with bitcoin</h2>
    <div class="rule"></div>
    <p>Neque porro quisquam est, qui dolorem ipsum quia dolor sit amet, consectetur, adipisci velit, sed quia non numquam eius modi tempora incidunt ut labore et dolore magnam aliquam quaerat voluptatem. Ut enim ad minima veniam, quis nostrum exercitationem.</p>
    <span class="btn">Create My Wallet</span>
  </div>
  <div class="wallet-art" role="img" aria-label="Laptop showing a bitcoin network illustration"></div>
</section>

<section class="ratings">
  <h2 class="section-title">5/5 Star Rating From Our Customers</h2>
  <div class="rule"></div>
  <div class="cards">
    <div class="card">
      <div class="card-box">
        <span class="card-icon"><svg width="22" height="20" viewBox="0 0 22 20"><path d="M2 2h18v12H9l-5 4v-4H2z" fill="none" stroke="#33a6d7" stroke-width="2"/></svg></span>
        Nemo enim ipsam voluptatem quia voluptas sit aspernatur aut odit aut fugit, sed quia consequuntur magni dolores eos qui ratione sequi nesciunt.
      </div>
      <h4>John Smith - Customer</h4>
      <div class="stars">★★★★★</div>
    </div>
    <div class="card featured">
      <div class="card-box">
        <span class="card-icon"><svg width="22" height="20" viewBox="0 0 22 20"><path d="M2 2h18v12H9l-5 4v-4H2z" fill="none" stroke="#33a6d7" stroke-width="2"/></svg></span>
        Nemo enim ipsam voluptatem quia voluptas sit aspernatur aut odit aut fugit, sed quia consequuntur magni dolores eos qui ratione sequi nesciunt.
      </div>
      <h4>Jemy - Customer</h4>
      <div class="stars">★★★★★</div>
    </div>
    <div class="card">
      <div class="card-box">
        <span class="card-icon"><svg width="22" height="20" viewBox="0 0 22 20"><path d="M2 2h18v12H9l-5 4v-4H2z" fill="none" stroke="#33a6d7" stroke-width="2"/></svg></span>
        Nemo enim ipsam voluptatem quia voluptas sit aspernatur aut odit aut fugit, sed quia consequuntur magni dolores eos qui ratione sequi nesciunt.
      </div>
      <h4>Elisa - Customer</h4>
      <div class="stars">★★★★★</div>
    </div>
  </div>
</section>

<section class="cta">
  <span>We offer an online bitcoin wallet and an KORVA prepaid card with which you can spend your bitcoins.</span>
  <span class="btn-outline">Join With Us</span>
</section>

<footer class="footer">
  <div class="brand"><span class="brand-mark"></span>Quarlen</div>
  <div class="social"><span></span><span></span><span></span><span></span><span></span></div>
  <ul class="footer-links">
    <li>HOME</li><li>QUARLEN FEATURES</li><li>FAQ</li><li>TESTIMONIALS</li><li>YOUR WALLET</li><li>RATINGS</li><li>CONTACT</li>
  </ul>
  <hr>
  <p class="copyright">Copyright © 2017 Quarlen. All Rights Reserved</p>
</footer>

</div>
</body>
</html>
```